Website Design for a flight comparison website wren skyways

m looking to build a flight quote website

The fields of the website should be

THE SITE WILL BE CALLED WREN SKYWAYS.

WHY USE WREN SKYWAYS

Widest choice of airfares on sale in the UK
Speak to an expert and take the stress out of
trawling the internet
Save your time and we will search for you
Our lowest airfare guarantee or fly for free
Let us customise the deal if you need flexibility

Ticket Type: Return / One Way

Class: Economy / Premium Economy / Business / First
From: AIRPORTS
To: AIRPORTS

Depart Date: dd/mm/yyyy
Return Date: dd/mm/yyyy

Adults:
Children:
Infants (under 2)

— NEXT PAGE—

-----------------------------------------------
Details of Lead Passenger

First Name:
Middle Name:
Surname:

DOB:

Address 1
Address 2
Town
County
Postcode

Email Adress:
Landline:
Mobile:
—————————————————————————

— NET PAGE —
Your Card Will Not Be Charged

Credit Card

16 digit
EXPIRY
CCV

DEBIT CARD
16 DIGIT
EXPIRY
CCV

SORT CODE
ACCOUNT NUMBER

—SUBMIT—

Thank you for using Wren Skyways.

Nothing needs to be too complicated just a one page website where users register their interest and then we will call them back offline.

Target Market(s)

People planning to travel last minute to all destinations worldwide.

Industry/Entity Type

Business

Requirements
Must have
• Be cool looking easy user interface.
Nice to have
• Parallax would be nice to make the site look modern and inline with todays websites.

```html
<!DOCTYPE html>
<html lang="en">
<head>
<meta charset="utf-8">
<title>Wren Skyways – Your Card Information</title>
<link rel="stylesheet" href="https://fonts.googleapis.com/css2?family=Lato:wght@400;700&family=Ubuntu:wght@500&display=swap">
<style>
  :root {
    --navy: #2e3d52;
    --nav-text: #aeb9c9;
    --white: #ffffff;
    --amber: #fbb71a;
    --field: #f1f1f1;
    --field-text: #a9a9a9;
    --label: #6d6d6d;
    --body-text: #3b3b3b;
    --rule: #ececec;
    --green: #97cf43;
    --footer-bg: #f4f4f4;
    --footer-text: #6a6a6a;
    --accent-blue: #1e88d6;
  }
  * { box-sizing: border-box; margin: 0; padding: 0; }
  html, body { width: 1200px; height: 905px; overflow: hidden; }
  body { position: relative; font-family: 'Lato', sans-serif; background: var(--white); }

  .site-header { position: absolute; left: 0; top: 0; width: 1200px; height: 82px; background: var(--navy); }
  .brand { position: absolute; display: flex; align-items: center; gap: 8px;
    font-family: 'Ubuntu', sans-serif; font-weight: 500; font-size: 24px; white-space: nowrap; }
  .brand-dot { width: 22px; height: 22px; border-radius: 50%; background: var(--amber); }
  .site-header .brand { left: 92px; top: 25px; color: var(--white); }
  .main-nav a { position: absolute; top: 36px; font-size: 10px; font-weight: 700;
    letter-spacing: .2px; color: var(--nav-text); text-decoration: none; text-transform: uppercase; white-space: nowrap; }
  .main-nav a.active { color: var(--white); }
  .social span { position: absolute; top: 37px; width: 9px; height: 9px; border-radius: 50%; background: var(--nav-text); }

  .hero { position: absolute; left: 0; top: 82px; width: 1200px; height: 772px;
    background: linear-gradient(180deg, #1f8fdc 0%, #4aaee6 35%, #9fd3ee 62%, #cbe6f2 78%, #b9dcec 100%); }

  .card-panel { position: absolute; left: 92px; top: 118px; width: 523px; height: 482px; background: var(--white); }
  .panel-head { height: 69px; background: var(--amber); color: var(--white); padding: 14px 22px; position: relative; }
  .panel-head h1 { font-size: 18px; font-weight: 700; line-height: 22px; }
  .panel-head p { font-size: 11px; letter-spacing: -.2px; }
  .panel-head svg { position: absolute; right: 22px; top: 24px; }

  .note { position: absolute; left: 22px; font-size: 12.5px; line-height: 15px; color: var(--body-text); letter-spacing: .2px; white-space: nowrap; }
  .label { position: absolute; font-size: 8.5px; line-height: 10px; color: var(--label); text-transform: uppercase; letter-spacing: .2px; white-space: nowrap; }
  .field { position: absolute; height: 30px; background: var(--field); color: var(--field-text);
    font-size: 10px; padding: 0 13px; line-height: 30px; white-space: nowrap; }
  .field.filled { color: #555; padding-left: 9px; }
  .field .toggle { position: absolute; right: 0; top: 0; width: 21px; height: 30px; background: var(--amber); }
  .field .toggle::after { content: ""; position: absolute; left: 8px; top: 13px; width: 5px; height: 3px;
    border-top: 1px solid #fde7a8; border-bottom: 1px solid #fde7a8; }
  .rule { position: absolute; left: 22px; width: 480px; height: 1px; background: var(--rule); }
  .submit { position: absolute; left: 22px; top: 396px; width: 480px; height: 29px; background: var(--green);
    color: var(--white); font-size: 10px; font-weight: 700; text-align: center; line-height: 29px; }

  .site-footer { position: absolute; left: 0; top: 854px; width: 1200px; height: 51px; background: var(--footer-bg); }
  .site-footer .brand { left: 92px; top: 12px; color: var(--navy); }
  .footer-links { position: absolute; right: 134px; top: 18px; font-size: 12px; line-height: 15px; color: var(--footer-text); white-space: nowrap; }
  .to-top { position: absolute; left: 1085px; top: 13px; width: 25px; height: 25px; border-radius: 50%;
    border: 1px solid var(--accent-blue); }
</style>
</head>
<body>
  <header class="site-header">
    <div class="brand"><span class="brand-dot"></span>Wren Skyways</div>
    <nav class="main-nav">
      <a class="active" href="#" style="left:463px">Home</a>
      <a href="#" style="left:534px">Flight Search</a>
      <a href="#" style="left:655px">About Us</a>
      <a href="#" style="left:746px">Contact Us</a>
      <a href="#" style="left:851px">Login</a>
      <a href="#" style="left:922px">Sign Up</a>
    </nav>
    <div class="social">
      <span style="left:994px"></span><span style="left:1025px"></span>
      <span style="left:1056px"></span><span style="left:1088px"></span>
    </div>
  </header>

  <div class="hero" role="img" aria-label="Sky and sea backdrop with a saluting flight attendant, a small palm island and airliners"></div>

  <section class="card-panel">
    <div class="panel-head">
      <h1>Your Card Information</h1>
      <p>We're bringing you a new level of comfort.</p>
      <svg width="42" height="22" viewBox="0 0 42 22" aria-hidden="true">
        <path d="M2 17 L40 3 L41 6 L10 19 Z M14 12 L8 6 L11 6 L20 10 Z M2 13 L0 10 L3 10 L6 14 Z" fill="#fff"/>
      </svg>
    </div>

    <p class="note" style="top:85px">Your Card Will Not Be Charged</p>

    <span class="label" style="left:22px;top:116px">Choose Card Type</span>
    <div class="field filled" style="left:22px;top:133px;width:231px">Credit Card<span class="toggle"></span></div>
    <span class="label" style="left:271px;top:116px">Card Number</span>
    <div class="field" style="left:271px;top:133px;width:231px">Enter 16 digit card number</div>

    <span class="label" style="left:23px;top:185px">Expiration Date</span>
    <div class="field filled" style="left:23px;top:202px;width:107px">month<span class="toggle"></span></div>
    <div class="field filled" style="left:148px;top:202px;width:106px">year<span class="toggle"></span></div>
    <span class="label" style="left:271px;top:185px">CCV</span>
    <div class="field filled" style="left:271px;top:202px;width:107px">enter CVV no<span class="toggle"></span></div>

    <div class="rule" style="top:249px"></div>

    <p class="note" style="top:276px;left:23px">Below details not required for Debit Card Users</p>

    <span class="label" style="left:23px;top:312px">Sort Code</span>
    <div class="field" style="left:23px;top:329px;width:231px">Enter 6 digit sort code</div>
    <span class="label" style="left:271px;top:312px">Account Number</span>
    <div class="field" style="left:271px;top:329px;width:232px">Enter 8 digit account number</div>

    <div class="rule" style="top:376px"></div>

    <div class="submit">SUBMIT</div>
  </section>

  <footer class="site-footer">
    <div class="brand"><span class="brand-dot"></span>Wren Skyways</div>
    <p class="footer-links">Home | About | Privacy Policy | Term of Use | © 2014 Wren Skyways</p>
    <div class="to-top">
      <svg width="23" height="23" viewBox="0 0 23 23" aria-hidden="true">
        <path d="M11.5 7 L11.5 16 M8.5 10 L11.5 7 L14.5 10" stroke="#1e3a5a" stroke-width="1.3" fill="none"/>
      </svg>
    </div>
  </footer>
</body>
</html>
```